Pellham Ridge Nectar Company, local Honey producer needs product Lable to encourage sales

We are a small business (Pellham Ridge Nectar Company) located in a small Texas town that harvests honey from our beehives yearly. Our honey would be considered "raw wildflower honey" and our goal is to sell it locally (farmers markets) and to surrounding areas.

We are currently packaging in plastic classic honey bottles with white flip caps. Sizes are 8oz and 16oz bottles (see pictures for actual size). Larger orders will be filled in one quart mason jars.

Design Ideas:
-vintage style design with bee or several bees in background
- incorporate company name "Pellham Ridge Nectar Company"
- needs small description "Raw Honey", and "Harvested in Bellville, Texas"

Target Market(s)

Farmers markets, health conscience people looking for unprocessed food options

Industry/Entity Type

Small Business

Requirements
Nice to have
• Vintage feel
Should not have
• No cartoonish characters

```html
<!DOCTYPE html>
<html lang="en">
<head>
<meta charset="utf-8">
<title>Raw Wildflower Honey – Pellham Ridge Nectar Company</title>
<link rel="stylesheet" href="https://fonts.googleapis.com/css2?family=Cinzel:wght@400;500&family=Open+Sans:wght@400;700&display=swap">
<style>
  :root {
    --page-bg: #ffffff;
    --title-brown: #3b1a14;
    --text-dark: #3a2a25;
    --band-brown: #3a0e0a;
    --band-text: #efe2b8;
    --band-subtext: #e8c672;
    --gold-light: #f6e3a1;
    --gold-mid: #d4a93f;
    --gold-dark: #9c7420;
    --parchment-light: #f4f3f1;
    --parchment-mid: #d9d8d5;
    --ornament: #4b3d38;
  }
  * { margin: 0; padding: 0; box-sizing: border-box; }
  html, body {
    width: 1091px;
    height: 1200px;
    overflow: hidden;
    background: var(--page-bg);
  }
  .canvas {
    position: relative;
    width: 1091px;
    height: 1200px;
  }
  .label {
    position: absolute;
    left: 235px;
    top: 150px;
    width: 620px;
    height: 900px;
  }
  .label-shape {
    position: absolute;
    inset: 0;
    width: 100%;
    height: 100%;
  }
  .label-text {
    position: absolute;
    left: 0;
    width: 100%;
    text-align: center;
  }
  .ornament {
    position: absolute;
    left: 50%;
    transform: translateX(-50%);
    width: 170px;
    height: 26px;
    border-radius: 13px;
    background: var(--ornament);
    opacity: 0.85;
  }
  .ornament--top { top: 62px; }
  .ornament--bottom { top: 372px; }
  .product-title {
    top: 100px;
    font-family: "Cinzel", serif;
    font-weight: 500;
    font-size: 70px;
    line-height: 84px;
    color: var(--title-brown);
  }
  .company-name {
    top: 418px;
    font-family: "Open Sans", sans-serif;
    font-size: 27px;
    color: var(--text-dark);
  }
  .band-title {
    top: 742px;
    font-family: "Cinzel", serif;
    font-size: 36px;
    line-height: 46px;
    color: var(--band-text);
  }
  .band-origin {
    top: 794px;
    left: 160px;
    width: 300px;
    font-family: "Open Sans", sans-serif;
    font-weight: 700;
    font-size: 20px;
    line-height: 25px;
    color: var(--band-subtext);
  }
</style>
</head>
<body>
<main class="canvas">
  <section class="label">
    <svg class="label-shape" viewBox="0 0 620 900" xmlns="http://www.w3.org/2000/svg">
      <defs>
        <clipPath id="label-oval">
          <ellipse cx="310" cy="450" rx="303" ry="443"/>
        </clipPath>
        <radialGradient id="parchment" cx="50%" cy="30%" r="70%">
          <stop offset="0" stop-color="#f4f3f1"/>
          <stop offset="1" stop-color="#d9d8d5"/>
        </radialGradient>
        <linearGradient id="honeycomb-tones" x1="0" y1="0" x2="1" y2="1">
          <stop offset="0" stop-color="#c9691a"/>
          <stop offset="0.45" stop-color="#f08a2a"/>
          <stop offset="0.75" stop-color="#e0561c"/>
          <stop offset="1" stop-color="#b8410f"/>
        </linearGradient>
        <linearGradient id="gold-frame" x1="0" y1="0" x2="1" y2="1">
          <stop offset="0" stop-color="#f6e3a1"/>
          <stop offset="0.4" stop-color="#d4a93f"/>
          <stop offset="0.7" stop-color="#f6e3a1"/>
          <stop offset="1" stop-color="#9c7420"/>
        </linearGradient>
      </defs>
      <g clip-path="url(#label-oval)">
        <rect class="label-parchment" x="0" y="0" width="620" height="900" fill="url(#parchment)"/>
        <rect class="label-illustration" x="0" y="470" width="620" height="260" fill="url(#honeycomb-tones)" role="img" aria-label="Honeycomb with a honey dipper and green mint leaves"/>
        <rect class="label-band" x="0" y="730" width="620" height="170" fill="#3a0e0a"/>
        <line x1="0" y1="730" x2="620" y2="730" stroke="#d4a93f" stroke-width="3"/>
      </g>
      <ellipse cx="310" cy="450" rx="303" ry="443" fill="none" stroke="url(#gold-frame)" stroke-width="12"/>
      <ellipse cx="310" cy="450" rx="294" ry="434" fill="none" stroke="#9c7420" stroke-width="1.5" opacity="0.7"/>
    </svg>

    <div class="ornament ornament--top" role="img" aria-label="Vintage flourish ornament"></div>
    <h1 class="label-text product-title">Raw<br>Wildflower<br>Honey</h1>
    <div class="ornament ornament--bottom" role="img" aria-label="Vintage flourish ornament"></div>
    <p class="label-text company-name">Pellham Ridge Nectar Company</p>
    <p class="label-text band-title">RAW HONEY</p>
    <p class="label-text band-origin">Harvested in Bellville,<br>Texas</p>
  </section>
</main>
</body>
</html>
```